Cedar Brook Stables, LLC

Equestrian business card to promote equine retirement, farm sitting, short term board. Located in Aiken, SC.
Updated color schemes.
Contact Information for Business Card
Contact info, description of work.
Colors
0094D4
00A9DD
6FCCEA
C7EBF8
E9F6FB
59FF00
82FF00
B8FF75
E3FFCB
F4FFEA
F0912C
F2A743
F7CA91
FBE8D2
FDF5EE

```html
<!DOCTYPE html>
<html lang="en">
<head>
<meta charset="UTF-8">
<title>Cedar Brook Stables, LLC – Business Card</title>
<link href="https://fonts.googleapis.com/css2?family=Poppins:wght@600;700&family=Arimo:wght@400&display=swap" rel="stylesheet">
<style>
  :root {
    --page-bg: #e9e6e4;
    --card-light: #e9f6fb;
    --card-dark: #262626;
    --band-blue: #0094d4;
    --accent-green: #59ff00;
    --brand-ink: #0094d4;
    --services-ink: #f0912c;
    --name-orange: #f0912c;
    --detail-orange: #f2a743;
    --icon-fill: #f7ca91;
    --divider: #c7ebf8;
  }
  html, body {
    margin: 0;
    width: 1200px;
    height: 900px;
    overflow: hidden;
    background: var(--page-bg);
  }
  .card {
    position: absolute;
    left: 100px;
    top: 140px;
    width: 1000px;
    height: 620px;
    background: var(--card-light);
    box-shadow: 0 14px 40px rgba(0,0,0,0.18);
    overflow: hidden;
  }
  .card-top {
    position: absolute;
    left: 0; top: 0;
    width: 100%;
    height: 354px;
    display: flex;
    flex-direction: column;
    align-items: center;
    justify-content: center;
    gap: 22px;
  }
  .brand {
    display: flex;
    align-items: center;
    gap: 18px;
  }
  .brand-dot {
    width: 30px;
    height: 30px;
    border-radius: 50%;
    background: var(--accent-green);
  }
  .brand-name {
    font-family: "Poppins", sans-serif;
    font-weight: 600;
    font-size: 40px;
    letter-spacing: 0.5px;
    color: var(--brand-ink);
    text-transform: uppercase;
  }
  .services {
    font-family: "Arimo", sans-serif;
    font-size: 24px;
    color: var(--services-ink);
    letter-spacing: 0.3px;
  }
  .card-band {
    position: absolute;
    left: 0; top: 354px;
    width: 100%;
    height: 10px;
    background: var(--band-blue);
  }
  .card-bottom {
    position: absolute;
    left: 0; top: 364px;
    width: 100%;
    height: 256px;
    background: var(--card-dark);
  }
  .person {
    position: absolute;
    right: 545px;
    top: 52px;
    text-align: right;
  }
  .person-name {
    font-family: "Poppins", sans-serif;
    font-weight: 700;
    font-size: 40px;
    line-height: 1;
    color: var(--name-orange);
    text-transform: uppercase;
    letter-spacing: 0.3px;
  }
  .person-role {
    font-family: "Arimo", sans-serif;
    font-size: 28px;
    color: var(--detail-orange);
    margin-top: 6px;
  }
  .divider {
    position: absolute;
    left: 493px;
    top: 50px;
    width: 2px;
    height: 96px;
    background: var(--divider);
  }
  .contacts {
    position: absolute;
    left: 521px;
    top: 46px;
    margin: 0;
    padding: 0;
    list-style: none;
  }
  .contact-item {
    display: flex;
    align-items: center;
    gap: 10px;
    height: 36px;
    font-family: "Arimo", sans-serif;
    font-size: 28px;
    color: var(--detail-orange);
  }
  .contact-icon {
    width: 26px;
    height: 26px;
    flex: none;
  }
  .address {
    position: absolute;
    left: 0;
    top: 180px;
    width: 100%;
    text-align: center;
    font-family: "Arimo", sans-serif;
    font-size: 28px;
    color: var(--detail-orange);
  }
</style>
</head>
<body>
  <div class="card">
    <div class="card-top">
      <div class="brand">
        <span class="brand-dot"></span>
        <span class="brand-name">Cedar Brook Stables, LLC</span>
      </div>
      <div class="services">Equine Retirement &nbsp;•&nbsp; Farm Sitting &nbsp;•&nbsp; Short-Term Board</div>
    </div>
    <div class="card-band"></div>
    <div class="card-bottom">
      <div class="person">
        <div class="person-name">Marcus Hale</div>
        <div class="person-role">Managing Director</div>
      </div>
      <div class="divider"></div>
      <ul class="contacts">
        <li class="contact-item">
          <svg class="contact-icon" viewBox="0 0 24 24" aria-hidden="true">
            <path fill="#f2a743" d="M6.6 10.8a15.1 15.1 0 0 0 6.6 6.6l2.2-2.2a1 1 0 0 1 1-.25 11.4 11.4 0 0 0 3.6.57 1 1 0 0 1 1 1V20a1 1 0 0 1-1 1A17 17 0 0 1 3 4a1 1 0 0 1 1-1h3.5a1 1 0 0 1 1 1c0 1.25.2 2.45.57 3.57a1 1 0 0 1-.25 1z"/>
          </svg>
          <span>803-555 019 274</span>
        </li>
        <li class="contact-item">
          <svg class="contact-icon" viewBox="0 0 24 24" aria-hidden="true">
            <rect x="2" y="5" width="20" height="14" fill="#f2a743"/>
            <path d="M2 5l10 8 10-8M2 19l7-7M22 19l-7-7" fill="none" stroke="#262626" stroke-width="1.5"/>
          </svg>
          <span>hello@cedarbrookstables.com</span>
        </li>
        <li class="contact-item">
          <svg class="contact-icon" viewBox="0 0 24 24" aria-hidden="true">
            <circle cx="12" cy="12" r="10" fill="#f2a743"/>
            <g fill="none" stroke="#262626" stroke-width="1.3">
              <ellipse cx="12" cy="12" rx="4.5" ry="10"/>
              <path d="M2 12h20M4 7h16M4 17h16M12 2v20"/>
            </g>
          </svg>
          <span>www.cedarbrookstables.com</span>
        </li>
      </ul>
      <div class="address">118, Whiskey Road, Aiken, SC 29801, USA</div>
    </div>
  </div>
</body>
</html>
```